Harbor Crest Home Surveys Brochure Design

Upscale Modern Clean Brochure. Our current brochure is about 11 inches high. I will be attaching the source files for our current design HarborSurveyPamphletV8HighRes (all of the information in this design will need to be in final product) . Its a booklet brochure and you can see the style and color or our branding ( For further branding or images please see harborcrestsurveys.example). We are interested in seeing variations of this layout as well as the same information in a bifold design like this example CommercialBrochureCover.png. Bifold design would be 4 total pages. Brochure design would be around 8 pages. Ive also included an older version of our brochure HC_TriFold_2020 (1)-edit (1). We are interested in seeing other front photos that would position us as an authority leader in the home inspection space.

Target Market(s)

Real Estate Agents

Industry/Entity Type

Home Inspections

Other font styles liked:
• https://filedrop.example/downloads/a1b2c3d4e5f60718293a4b5c6d7e8f9020221012222612/0f1e2d3c4b5a69788796a5b4c3d2e1f020221012222646/7c9e41

Requirements
Must have
• Branded colors of blue that is in our Logo- All of the information that is in the HarborSurveyPamphletV8LowRes- There is also a filedrop link under the font section that can download source files for this brochure

```html
<!DOCTYPE html>
<html lang="en">
<head>
<meta charset="utf-8">
<title>Harbor Crest Home Surveys – Bifold Brochure</title>
<link rel="stylesheet" href="https://fonts.googleapis.com/css2?family=Montserrat:wght@400;500;600;700;800&display=swap">
<style>
  :root {
    --brand-blue: #0a66b8;
    --brand-blue-deep: #0659a6;
    --ink: #1d1d1f;
    --paper: #ffffff;
    --stage: #d4d4d6;
    --photo-sky: #c9cdd2;
    --photo-grass: #7da24a;
  }
  * { box-sizing: border-box; margin: 0; padding: 0; }
  html, body { width: 831px; height: 1200px; overflow: hidden; }
  body {
    background: var(--stage);
    font-family: "Montserrat", sans-serif;
    color: var(--ink);
    position: relative;
  }
  .spread {
    position: absolute; left: 15px; top: 341px;
    width: 800px; height: 518px;
    background: var(--paper);
    box-shadow: 0 6px 18px rgba(0,0,0,.25);
    overflow: hidden;
  }
  .abs { position: absolute; }

  /* Guarantees column */
  .guarantee-title { left: 42px; top: 50px; width: 165px; font-weight: 800; font-size: 10.6px; line-height: 1; letter-spacing: .1px; white-space: nowrap; }
  .guarantee-tag {
    left: 43px; top: 66px; width: 129px; height: 20px;
    background: var(--brand-blue); color: #fff;
    font-weight: 800; font-size: 14.5px; line-height: 20px; text-align: center; letter-spacing: .4px;
  }
  .small-copy { font-size: 6.3px; line-height: 1.3; font-weight: 500; }
  .guarantee-intro { left: 43px; top: 95px; width: 135px; }
  .guarantee-list { left: 43px; top: 123px; list-style: none; font-size: 5.6px; font-weight: 700; line-height: 1.75; }
  .guarantee-list li { display: flex; align-items: center; gap: 3px; }
  .guarantee-list svg { width: 5px; height: 5px; flex: none; }
  .guarantee-body { left: 43px; top: 172px; width: 135px; }
  .badges { left: 43px; top: 268px; display: flex; gap: 6px; }
  .badge { width: 26px; height: 26px; border-radius: 50%; }
  .badge.gold { background: #c9a53a; }
  .badge.red { background: #c0302e; }
  .badge.green { background: #6a9a4c; width: 36px; border-radius: 13px; }
  .badge.ring { background: none; border: 4px solid #e04a6a; }

  /* Reviews column */
  .reviews-title { left: 218px; top: 48px; font-size: 10.5px; font-weight: 700; line-height: 1.4; }
  .reviews-title em { font-style: normal; color: var(--brand-blue); }
  .reviews-rule { left: 218px; top: 94px; width: 26px; height: 2px; background: var(--brand-blue); }
  .review { left: 218px; width: 135px; }
  .review .q { color: #bcbcbc; font-size: 14px; font-weight: 800; line-height: .8; display: block; height: 10px; font-family: Georgia, serif; }
  .review .by { text-align: right; color: var(--brand-blue); font-weight: 700; font-size: 6.5px; margin-top: 4px; padding-right: 18px; }

  /* Blue bands */
  .band { top: 309px; height: 158px; background: var(--brand-blue); }
  .band-left { left: 0; width: 400px; border-bottom-right-radius: 18px; }
  .band-right { left: 400px; width: 400px; border-bottom-right-radius: 18px; }

  .contact-title { left: 42px; top: 337px; color: #fff; font-weight: 600; font-size: 14px; }
  .contact-rule { left: 42px; top: 358px; width: 26px; height: 1.5px; background: #fff; }
  .contact-list { left: 30px; top: 370px; list-style: none; color: #fff; font-size: 8.5px; line-height: 1.4; font-weight: 500; }
  .contact-list li { display: flex; gap: 5px; margin-bottom: 3px; }
  .contact-list svg { width: 7px; height: 7px; margin-top: 2px; flex: none; }

  .band-mark { left: 260px; top: 342px; width: 100px; text-align: center; color: #fff; }
  .band-mark .dot { width: 30px; height: 30px; border-radius: 50%; border: 2px solid #fff; margin: 0 auto 5px; }
  .band-mark .name { font-weight: 800; font-size: 9px; letter-spacing: .3px; }
  .partners { left: 250px; top: 430px; display: flex; gap: 14px; color: #fff; font-size: 8.5px; font-weight: 600; }
  .partners span small { display: block; font-size: 3.8px; font-weight: 500; letter-spacing: .3px; }

  /* Cover */
  .cover-photo {
    left: 400px; top: 76px; width: 400px; height: 233px;
    background: linear-gradient(180deg, #fff 0%, var(--photo-sky) 22%, #9ea6ad 55%, #8aa55a 82%, var(--photo-grass) 100%);
  }
  .cover-mark { left: 470px; top: 22px; display: flex; align-items: center; gap: 8px; z-index: 2; }
  .cover-mark .dot { width: 44px; height: 44px; border-radius: 50%; background: var(--brand-blue); flex: none; }
  .cover-mark .name { color: var(--brand-blue); font-weight: 800; font-size: 19px; line-height: 1; letter-spacing: .4px; }
  .cover-mark .name small { display: block; font-size: 6.5px; font-weight: 800; letter-spacing: .8px; margin-top: 4px; }
  .cover-title { left: 458px; top: 333px; color: #fff; font-weight: 800; font-size: 20.5px; line-height: 1.27; letter-spacing: .3px; }
  .cover-sub { left: 458px; top: 418px; color: #fff; font-size: 9.3px; line-height: 1.3; font-weight: 500; padding-left: 10px; border-left: 1.5px solid #fff; }
  .cover-ghost { left: 700px; top: 405px; width: 70px; height: 70px; border-radius: 50%; border: 2px solid rgba(255,255,255,.12); }

  .footer-cta { left: 42px; top: 482px; font-size: 9px; font-weight: 700; color: var(--ink); }
  .footer-cta em { font-style: normal; color: var(--brand-blue); }
  .footer-web { left: 617px; top: 481px; font-size: 8.5px; font-weight: 600; }
  .footer-web em { font-style: normal; color: var(--brand-blue); }
</style>
</head>
<body>
<main class="spread">

  <h2 class="abs guarantee-title">HARBOR CREST’S 100-DAY</h2>
  <div class="abs guarantee-tag">GUARANTEES</div>
  <p class="abs small-copy guarantee-intro">Every Harbor Crest inspection comes complete with these 100-day guarantees for the homebuyer:</p>
  <ul class="abs guarantee-list">
    <li><svg viewBox="0 0 10 10"><circle cx="5" cy="5" r="4.3" fill="none" stroke="#0a66b8" stroke-width="1"/><path d="M3 5.2l1.4 1.4L7 3.8" fill="none" stroke="#0a66b8" stroke-width="1"/></svg>Structure &amp; Mechanical Guarantee</li>
    <li><svg viewBox="0 0 10 10"><circle cx="5" cy="5" r="4.3" fill="none" stroke="#0a66b8" stroke-width="1"/><path d="M3 5.2l1.4 1.4L7 3.8" fill="none" stroke="#0a66b8" stroke-width="1"/></svg>Roof Condition &amp; No-Leak Guarantee</li>
    <li><svg viewBox="0 0 10 10"><circle cx="5" cy="5" r="4.3" fill="none" stroke="#0a66b8" stroke-width="1"/><path d="M3 5.2l1.4 1.4L7 3.8" fill="none" stroke="#0a66b8" stroke-width="1"/></svg>Mold-Free Guarantee</li>
    <li><svg viewBox="0 0 10 10"><circle cx="5" cy="5" r="4.3" fill="none" stroke="#0a66b8" stroke-width="1"/><path d="M3 5.2l1.4 1.4L7 3.8" fill="none" stroke="#0a66b8" stroke-width="1"/></svg>Underground Sewer/Water Line Guarantee</li>
  </ul>
  <p class="abs small-copy guarantee-body">With these guarantees in place, homeowners have the assurance that if our inspector missed a defect that caused a covered system to fail within 100 days of the inspection, Harbor Crest will cover up to $500 toward repairs. This assurance provides peace-of-mind for homeowners and their agents.</p>
  <div class="abs badges" aria-label="Certification badges">
    <span class="badge gold"></span><span class="badge red"></span><span class="badge green"></span><span class="badge ring"></span>
  </div>

  <h3 class="abs reviews-title">Harbor Crest has<br>earned over <em>5,000 5-star<br>customer reviews!</em></h3>
  <div class="abs reviews-rule"></div>
  <blockquote class="abs review small-copy" style="top:103px">
    <span class="q">“</span>
    I am extremely pleased with the property inspection I recently received. Very thorough, very professional, and the report was prepared and delivered to my agent and me overnight!
    <div class="by">–Dana R</div>
  </blockquote>
  <blockquote class="abs review small-copy" style="top:168px">
    <span class="q">“</span>
    The Harbor Crest group is at the top of my list for home inspections. The overall performance on every inspection that they have completed for my clients speaks for itself. This is why they continue to be referred to my clients.
    <div class="by">–Luis P.</div>
  </blockquote>
  <blockquote class="abs review small-copy" style="top:241px">
    <span class="q">“</span>
    Harbor Crest’s inspector was great -- very helpful, answered all my questions and also provided useful information.
    <div class="by">–Omar T.</div>
  </blockquote>

  <div class="abs band band-left"></div>
  <div class="abs band band-right"></div>

  <h3 class="abs contact-title">Contact Info</h3>
  <div class="abs contact-rule"></div>
  <ul class="abs contact-list">
    <li><svg viewBox="0 0 10 10"><circle cx="5" cy="3.5" r="2.3" fill="none" stroke="#fff"/><path d="M5 5.8V10" stroke="#fff"/></svg><span>2150 Marlow Ave Ste 310<br>Alder Point, CA 90000</span></li>
    <li><svg viewBox="0 0 10 10"><rect x="1" y="2.5" width="8" height="5.5" fill="none" stroke="#fff"/><path d="M1 2.5l4 3 4-3" fill="none" stroke="#fff"/></svg><span>customerservice@harborcrestsurveys.example</span></li>
    <li><svg viewBox="0 0 10 10"><circle cx="5" cy="5" r="4" fill="none" stroke="#fff"/><path d="M3.5 3l1 1.5-.6.8 1.5 1.5.8-.6L7.5 7" fill="none" stroke="#fff" stroke-width=".8"/></svg><span>(800) 555-0142</span></li>
    <li><svg viewBox="0 0 10 10"><circle cx="5" cy="5" r="4" fill="none" stroke="#fff"/><path d="M1 5h8M5 1c-2 2.5-2 5.5 0 8M5 1c2 2.5 2 5.5 0 8" fill="none" stroke="#fff" stroke-width=".7"/></svg><span>www.harborcrestsurveys.example</span></li>
  </ul>

  <div class="abs band-mark">
    <div class="dot"></div>
    <div class="name">HARBOR CREST</div>
  </div>
  <div class="abs partners">
    <span>HomeFinder<small>REVIEWS ★★★★★</small></span>
    <span>Searchly<small>REVIEWS ★★★★★</small></span>
  </div>

  <div class="abs cover-photo" role="img" aria-label="Photo of a family walking toward a suburban house with a for-sale sign on the lawn"></div>
  <div class="abs cover-mark">
    <span class="dot"></span>
    <span class="name">HARBOR CREST<small>HOME SURVEYS</small></span>
  </div>

  <h1 class="abs cover-title">SOUTHERN CALIFORNIA’S<br>LARGEST HOME<br>INSPECTION COMPANY</h1>
  <p class="abs cover-sub">Providing homebuyers and sellers<br>peace of mind since 1984</p>
  <div class="abs cover-ghost"></div>

  <p class="abs footer-cta"><em>Get a Quote or Schedule an Inspection Today!</em> (866) 555-0187</p>
  <p class="abs footer-web">www.<em>harborcrestsurveys</em>.example</p>
</main>
</body>
</html>
```